Fernvale Pharmacy opening

We want to have a double sided 5.5"x8.5" flyer for a new Pharmacy opening in a well known strip mall in the neighborhood and we are planning to mail it to neighbors homes.

Want to put the outside pharmacy picture on the main side of the flyer and a coupon with 25% off towards an OTC product on the back in addition to the info below (preferably in a sort of bulletin points not a list (something like the 2 examples attached).

Colors to be red like the exterior sign and blue like the interior wall paint:

Front side should have:
Fernvale pharmacy
Your locally owned and operated pharmacy around the corner.
317-4082 Tarrow rd.
Brisket hollow plaza
T. 604 827 5530 (call or text)
F. 604-827-5532

Free prescription delivery
Text us for refills
Specialized compounding
Customized compression stockings

The back side should have:

Do you forget taking your medications! We offer multiple compliance packaging options at no additional cost.
Had shingles before or worried to have it? travelling soon? check our vaccinations options!
Suffering side effects? We are experienced to check your medications interactions & different coverage options.
Hard time monitoring your blood pressure? Trying to stop smoking? we can always help.

FEELING BETTER STARTS HERE

```html
<!DOCTYPE html>
<html lang="en">
<head>
<meta charset="utf-8">
<title>Fernvale Pharmacy – Grand Opening Flyer</title>
<link rel="stylesheet" href="https://fonts.googleapis.com/css2?family=Anton&family=Montserrat:wght@500;600;700;800;900&display=swap">
<style>
  :root {
    --red: #d81f26;
    --red-dark: #a3121a;
    --gold-light: #ffe27a;
    --gold: #f4b81c;
    --gold-dark: #b57a06;
    --ink: #1c1c1c;
    --night: #0c1016;
    --white: #ffffff;
    --grey: #3a3a3a;
    --page: #eef0f3;
  }
  * { margin: 0; padding: 0; box-sizing: border-box; }
  html, body { width: 784px; height: 1200px; overflow: hidden; background: var(--page); }
  body { font-family: "Montserrat", Arial, sans-serif; color: var(--ink); }

  .spread {
    width: 784px; height: 1200px;
    display: flex; justify-content: center; align-items: center; gap: 16px;
  }
  .flyer { position: relative; width: 370px; height: 572px; overflow: hidden; background: var(--white); }

  /* shared */
  .swoosh { position: absolute; left: 0; width: 370px; }
  .contact-bar {
    position: absolute; left: 0; bottom: 0; width: 100%; height: 54px;
    background: var(--night); color: var(--white);
    display: flex; justify-content: space-between; align-items: center; padding: 0 14px;
    font-size: 9.5px; font-weight: 600; line-height: 1.45;
  }
  .contact-item { display: flex; align-items: center; gap: 7px; }
  .contact-icon { flex: 0 0 18px; width: 18px; height: 18px; border-radius: 50%; background: var(--red); display: flex; align-items: center; justify-content: center; }

  /* front */
  .store-photo {
    position: absolute; left: 0; top: 0; width: 370px; height: 300px;
    background:
      radial-gradient(ellipse at 50% 55%, rgba(120,140,160,.35), transparent 65%),
      linear-gradient(180deg, #10151d 0%, #263140 45%, #3d4a58 75%, #1a2028 100%);
  }
  .brand { position: absolute; left: 0; width: 100%; display: flex; justify-content: center; align-items: center; gap: 7px; }
  .front .brand { top: 20px; }
  .brand-dot { width: 20px; height: 20px; border-radius: 50%; background: var(--red); }
  .brand-name { font-weight: 800; font-size: 12px; letter-spacing: .5px; color: var(--white); }
  .headline {
    position: absolute; top: 54px; left: 0; width: 100%; text-align: center;
    font-family: "Anton", Impact, sans-serif; font-weight: 400; text-transform: uppercase;
    font-size: 70px; line-height: 0.98; letter-spacing: 1px;
    background: linear-gradient(180deg, var(--gold-light) 0%, var(--gold) 50%, var(--gold-dark) 100%);
    -webkit-background-clip: text; background-clip: text; color: transparent;
  }
  .store-name {
    position: absolute; top: 204px; left: 0; width: 100%; text-align: center;
    font-weight: 800; font-size: 14px; letter-spacing: 1px; color: var(--white); text-transform: uppercase;
  }
  .front .swoosh { top: 236px; height: 92px; }
  .tagline { position: absolute; top: 334px; left: 0; width: 100%; text-align: center; text-transform: uppercase; font-weight: 900; }
  .tagline .line-dark { display: block; font-size: 18px; line-height: 1.2; color: var(--ink); }
  .tagline .line-red { display: block; font-size: 23px; line-height: 1.1; color: var(--red); }
  .services {
    position: absolute; top: 420px; left: 30px; width: 310px;
    display: grid; grid-template-columns: 1fr 1fr; row-gap: 14px; column-gap: 12px; list-style: none;
  }
  .service { display: flex; align-items: center; gap: 8px; font-weight: 700; font-size: 10.5px; line-height: 1.2; color: var(--grey); }
  .service-icon { flex: 0 0 26px; width: 26px; height: 26px; border-radius: 50%; background: var(--red); display: flex; align-items: center; justify-content: center; }

  /* back */
  .pharmacist-photo {
    position: absolute; left: 0; top: 0; width: 370px; height: 236px;
    background: linear-gradient(180deg, #dfe9f3 0%, #b9cde0 55%, #9fb6cc 100%);
  }
  .coupon {
    position: absolute; left: 16px; top: 46px; width: 116px; height: 116px; border-radius: 50%;
    background: var(--red); color: var(--white); border: 3px solid var(--white);
    display: flex; flex-direction: column; align-items: center; justify-content: center; text-align: center;
  }
  .coupon-value { font-family: "Anton", Impact, sans-serif; font-size: 36px; line-height: 1; }
  .coupon-off { font-weight: 900; font-size: 14px; line-height: 1.1; }
  .coupon-terms { font-weight: 600; font-size: 8px; line-height: 1.25; margin-top: 3px; }
  .back .swoosh { top: 176px; height: 80px; }
  .back .brand { top: 250px; }
  .back .brand-name { color: var(--ink); font-size: 11px; }
  .back .brand-dot { width: 16px; height: 16px; }
  .tips { position: absolute; top: 282px; left: 20px; width: 330px; list-style: none; }
  .tip { display: flex; gap: 8px; margin-bottom: 11px; }
  .tip-icon { flex: 0 0 16px; width: 16px; height: 16px; margin-top: 1px; border-radius: 50%; background: var(--red); display: flex; align-items: center; justify-content: center; }
  .tip-question { display: block; font-weight: 800; font-size: 10.5px; line-height: 1.25; color: var(--red); }
  .tip-answer { display: block; font-weight: 600; font-size: 9.5px; line-height: 1.3; color: var(--grey); }
  .slogan {
    position: absolute; top: 486px; left: 0; width: 100%; text-align: center;
    font-weight: 900; font-size: 14px; letter-spacing: .5px; color: var(--ink);
  }
</style>
</head>
<body>
<main class="spread">

  <!-- Front side -->
  <section class="flyer front">
    <div class="store-photo" role="img" aria-label="Photo of the pharmacy storefront and interior shelves"></div>
    <div class="brand">
      <span class="brand-dot"></span>
      <span class="brand-name">Fernvale Pharmacy</span>
    </div>
    <h1 class="headline">Grand<br>Opening</h1>
    <p class="store-name">Fernvale Pharmacy</p>

    <svg class="swoosh" viewBox="0 0 784 190" preserveAspectRatio="none" aria-hidden="true">
      <path d="M0 60 C 200 150, 560 150, 784 50 L784 190 L0 190 Z" fill="var(--red-dark)"/>
      <path d="M0 90 C 220 170, 560 170, 784 80 L784 190 L0 190 Z" fill="var(--red)"/>
      <path d="M0 130 C 240 200, 560 200, 784 120 L784 190 L0 190 Z" fill="var(--white)"/>
    </svg>

    <h2 class="tagline">
      <span class="line-dark">Your locally owned and</span>
      <span class="line-red">Operated pharmacy</span>
      <span class="line-dark">Around the corner</span>
    </h2>

    <ul class="services">
      <li class="service">
        <span class="service-icon"><svg width="14" height="14" viewBox="0 0 24 24"><path d="M1 6h13v9H1zM14 9h4l3 3v3h-7z" fill="#fff"/><circle cx="5" cy="17" r="2" fill="#fff"/><circle cx="17" cy="17" r="2" fill="#fff"/></svg></span>
        Free prescription delivery
      </li>
      <li class="service">
        <span class="service-icon"><svg width="14" height="14" viewBox="0 0 24 24"><path d="M6 12l4 4 8-9" stroke="#fff" stroke-width="3" fill="none" stroke-linecap="round"/></svg></span>
        Specialized compounding
      </li>
      <li class="service">
        <span class="service-icon"><svg width="14" height="14" viewBox="0 0 24 24"><path d="M3 4h18v12H8l-5 4z" fill="#fff"/></svg></span>
        Text us for refills
      </li>
      <li class="service">
        <span class="service-icon"><svg width="14" height="14" viewBox="0 0 24 24"><path d="M6 12l4 4 8-9" stroke="#fff" stroke-width="3" fill="none" stroke-linecap="round"/></svg></span>
        Customized compression stockings
      </li>
    </ul>

    <footer class="contact-bar">
      <div class="contact-item">
        <span class="contact-icon"><svg width="10" height="10" viewBox="0 0 24 24"><path d="M6 2l4 4-2 3c1 3 4 6 7 7l3-2 4 4-3 4C10 22 2 14 2 5z" fill="#fff"/></svg></span>
        <span>T. 604 827 5530 (call or text)<br>F. 604-827-5532</span>
      </div>
      <div class="contact-item">
        <span class="contact-icon"><svg width="10" height="10" viewBox="0 0 24 24"><path d="M12 2a7 7 0 0 0-7 7c0 5 7 13 7 13s7-8 7-13a7 7 0 0 0-7-7z" fill="#fff"/></svg></span>
        <span>317-4082 Tarrow rd.<br>Brisket hollow plaza</span>
      </div>
    </footer>
  </section>

  <!-- Back side -->
  <section class="flyer back">
    <div class="pharmacist-photo" role="img" aria-label="Photo of a smiling pharmacist in a white coat in front of pharmacy shelves"></div>

    <div class="coupon">
      <span class="coupon-value">25%</span>
      <span class="coupon-off">OFF</span>
      <span class="coupon-terms">Towards an<br>OTC product</span>
    </div>

    <svg class="swoosh" viewBox="0 0 784 190" preserveAspectRatio="none" aria-hidden="true">
      <path d="M0 60 C 200 150, 560 150, 784 50 L784 190 L0 190 Z" fill="var(--red-dark)"/>
      <path d="M0 90 C 220 170, 560 170, 784 80 L784 190 L0 190 Z" fill="var(--red)"/>
      <path d="M0 130 C 240 200, 560 200, 784 120 L784 190 L0 190 Z" fill="var(--white)"/>
    </svg>

    <div class="brand">
      <span class="brand-dot"></span>
      <span class="brand-name">Fernvale Pharmacy</span>
    </div>

    <ul class="tips">
      <li class="tip">
        <span class="tip-icon"><svg width="9" height="9" viewBox="0 0 24 24"><path d="M5 12l5 5 9-10" stroke="#fff" stroke-width="4" fill="none" stroke-linecap="round"/></svg></span>
        <p><span class="tip-question">Do you forget taking your medications!</span>
        <span class="tip-answer">We offer multiple compliance packaging options at no additional cost.</span></p>
      </li>
      <li class="tip">
        <span class="tip-icon"><svg width="9" height="9" viewBox="0 0 24 24"><path d="M5 12l5 5 9-10" stroke="#fff" stroke-width="4" fill="none" stroke-linecap="round"/></svg></span>
        <p><span class="tip-question">Had shingles before or worried to have it? Travelling soon?</span>
        <span class="tip-answer">Check our vaccinations options!</span></p>
      </li>
      <li class="tip">
        <span class="tip-icon"><svg width="9" height="9" viewBox="0 0 24 24"><path d="M5 12l5 5 9-10" stroke="#fff" stroke-width="4" fill="none" stroke-linecap="round"/></svg></span>
        <p><span class="tip-question">Suffering side effects?</span>
        <span class="tip-answer">We are experienced to check your medications interactions &amp; different coverage options.</span></p>
      </li>
      <li class="tip">
        <span class="tip-icon"><svg width="9" height="9" viewBox="0 0 24 24"><path d="M5 12l5 5 9-10" stroke="#fff" stroke-width="4" fill="none" stroke-linecap="round"/></svg></span>
        <p><span class="tip-question">Hard time monitoring your blood pressure? Trying to stop smoking?</span>
        <span class="tip-answer">We can always help.</span></p>
      </li>
    </ul>

    <p class="slogan">FEELING BETTER STARTS HERE</p>

    <footer class="contact-bar">
      <div class="contact-item">
        <span class="contact-icon"><svg width="10" height="10" viewBox="0 0 24 24"><path d="M6 2l4 4-2 3c1 3 4 6 7 7l3-2 4 4-3 4C10 22 2 14 2 5z" fill="#fff"/></svg></span>
        <span>T. 604 827 5530 (call or text)<br>F. 604-827-5532</span>
      </div>
      <div class="contact-item">
        <span class="contact-icon"><svg width="10" height="10" viewBox="0 0 24 24"><path d="M12 2a7 7 0 0 0-7 7c0 5 7 13 7 13s7-8 7-13a7 7 0 0 0-7-7z" fill="#fff"/></svg></span>
        <span>317-4082 Tarrow rd.<br>Brisket hollow plaza</span>
      </div>
    </footer>
  </section>

</main>
</body>
</html>
```